Life Coaching and Career Coaching company needs new website with bold, modern, videos

We need a whole new website that is heavy on video. We are a small company who sells personal wellbeing services like career coaching, life coaching, and group coaching programs. The programs all help people design a better life.
FULL BRIEF ATTACHED and STYLE GUIDE
Also, look at https://www.pinevaultery.com/coaching and corvanly.com and https://www.tarnwick.life/ for a small amount of inspiration.

Industry/Entity Type

personal well-being/life coaching/career coaching

Number of Pages Required

3 page

Other font styles liked:
• fonts are in the brief

Requirements
Must have
• read the brief please - it's all in there. (things like the look, feel, how it will have lots of video, etc,)
Nice to have
• something really different looking and breakthrough. visually stunning. very trustworthy. Please read the brief, its all in there.
Should not have
• should not look like other life coaching websites. must have video!

```html
<!DOCTYPE html>
<html lang="en">
<head>
<meta charset="utf-8">
<title>Brightpath Studio — Life &amp; Career Coaching</title>
<link rel="stylesheet" href="https://fonts.googleapis.com/css2?family=Righteous&family=Questrial&display=swap">
<style>
:root{
  --coral:#ef6461;
  --coral-dark:#e4524f;
  --ink:#1d1d1f;
  --text:#6f6f74;
  --muted:#9a9a9f;
  --light:#f5f5f6;
  --white:#ffffff;
  --black:#0c0c0d;
  --display:'Righteous',sans-serif;
  --body:'Questrial',sans-serif;
}
*{box-sizing:border-box;margin:0;padding:0}
html,body{width:1200px;height:3702px;overflow:hidden}
body{position:relative;font-family:var(--body);color:var(--ink);background:var(--white)}
.abs{position:absolute}

/* header */
.site-header{position:absolute;top:0;left:0;width:1200px;height:62px;background:var(--white);z-index:5}
.brand{position:absolute;left:172px;top:16px;font-family:var(--body);font-size:24px;letter-spacing:1px;color:#6b6b70;display:flex;align-items:center;gap:6px}
.brand .mark{width:10px;height:10px;border-radius:50%;background:var(--coral)}
.main-nav{position:absolute;left:460px;top:24px;display:flex;gap:30px;font-size:13px;color:#555}
.main-nav .active{color:var(--coral);font-weight:bold;position:relative}
.main-nav .active::before{content:"";position:absolute;left:15px;top:-10px;width:6px;height:6px;border-left:1.5px solid var(--coral);border-top:1.5px solid var(--coral);transform:rotate(45deg)}
.header-cta{position:absolute;right:0;top:0;width:286px;height:62px;background:var(--coral);color:var(--white);font-family:var(--display);font-size:16px;display:flex;align-items:center;padding-left:76px}
.header-cta .bubble{position:absolute;left:24px;top:16px;width:32px;height:30px;border-radius:50%;background:var(--white)}
.header-cta .bubble::after{content:"•••";position:absolute;left:6px;top:6px;color:var(--coral);font-size:12px;letter-spacing:1px}

/* hero */
.hero{position:absolute;top:62px;left:0;width:1200px;height:745px;background:linear-gradient(110deg,#6d5a44 0%,#8c7a62 30%,#b6aa98 55%,#8d8476 80%,#5d5245 100%)}
.hero::after{content:"";position:absolute;inset:0;background:linear-gradient(90deg,rgba(0,0,0,.35),rgba(0,0,0,0) 60%)}
.hero-copy{position:absolute;left:174px;top:184px;z-index:2;color:var(--white)}
.hero-kicker{font-family:var(--display);font-size:13px}
.hero-title{font-family:var(--display);font-weight:400;font-size:34px;line-height:45px;margin-top:18px;width:520px}
.btn{display:inline-flex;align-items:center;gap:14px;border-radius:24px;background:var(--coral);color:var(--white);font-family:var(--display)}
.hero-btn{margin-top:22px;height:48px;padding:0 26px;font-size:14px}
.chev{width:8px;height:8px;border-right:2px solid currentColor;border-top:2px solid currentColor;transform:rotate(45deg)}
.follow{position:absolute;left:54px;top:270px;z-index:2;color:var(--white);font-size:11px;writing-mode:vertical-rl;transform:rotate(180deg)}
.follow-line{position:absolute;left:60px;top:340px;width:1px;height:50px;background:rgba(255,255,255,.7);z-index:2}
.follow-icons{position:absolute;left:56px;top:408px;z-index:2;display:flex;flex-direction:column;gap:14px}
.follow-icons span{width:10px;height:10px;border-radius:2px;background:var(--white)}
.play-video{position:absolute;left:1068px;top:326px;z-index:2;width:34px;height:34px;border-radius:50%;background:var(--coral)}
.play-video::after,.play::after{content:"";position:absolute;left:50%;top:50%;transform:translate(-35%,-50%);border-left:9px solid var(--white);border-top:6px solid transparent;border-bottom:6px solid transparent}
.play-label{position:absolute;left:1078px;top:372px;z-index:2;color:var(--white);font-size:10px;writing-mode:vertical-rl}
.play-arrow{position:absolute;left:1085px;top:420px;z-index:2;width:1px;height:44px;background:var(--white)}
.hero-curve{position:absolute;left:0;top:690px;z-index:3}

/* section titles */
.section-title{position:absolute;left:0;width:1200px;text-align:center;font-family:var(--display);font-weight:400;font-size:26px}

/* programs */
.program{position:absolute;width:417px;height:315px;border-radius:18px;overflow:hidden}
.program .label{position:absolute;left:24px;bottom:20px;color:var(--white);font-family:var(--display);font-size:19px}
.program .shade{position:absolute;inset:0;background:linear-gradient(180deg,rgba(0,0,0,0) 55%,rgba(0,0,0,.45))}
.play{position:absolute;width:28px;height:28px;border-radius:50%;background:var(--coral)}
.play::after{border-left-width:7px;border-top-width:5px;border-bottom-width:5px}
.program .play{right:28px;bottom:16px}
.play-lg{left:181px;top:128px;width:56px;height:56px}
.play-lg::after{border-left-width:14px;border-top-width:9px;border-bottom-width:9px}
.notch{position:absolute;left:541px;top:1128px;width:54px;height:54px;border-radius:50%;background:var(--white)}
.notch-btn{position:absolute;left:546px;top:1133px;width:44px;height:44px;border-radius:50%;background:var(--coral)}
.notch-btn::after{content:"";position:absolute;left:16px;top:16px;width:9px;height:9px;border-top:2px solid var(--white);border-right:2px solid var(--white)}

/* how it works */
.how{position:absolute;top:1611px;left:0;width:1200px;height:423px;background:var(--coral)}
.how .section-title{top:50px;color:var(--white)}
.step{position:absolute;top:138px;width:200px;text-align:center;color:var(--white)}
.step .icon{position:relative;margin:0 auto;width:68px;height:68px;border-radius:50%;background:var(--white)}
.step .num{position:absolute;left:-8px;top:-6px;width:26px;height:26px;border-radius:50%;background:var(--coral-dark);border:2px solid var(--white);font-size:11px;line-height:22px;text-align:center;color:var(--white)}
.step h3{font-family:var(--display);font-weight:400;font-size:12px;margin-top:26px;letter-spacing:.3px}
.step p{font-size:11px;line-height:18px;margin-top:6px;opacity:.95}
.how-btn{position:absolute;left:481px;top:329px;height:46px;padding:0 26px;border:1.5px solid rgba(255,255,255,.8);background:var(--coral-dark);font-size:15px}

/* who we are */
.dots{position:absolute;display:grid;gap:24px 30px}
.dots i{width:4px;height:4px;border-radius:50%;background:var(--coral)}
.who-title{position:absolute;left:685px;top:2110px;font-family:var(--display);font-weight:400;font-size:26px}
.who-text{position:absolute;left:685px;width:345px;font-size:12px;line-height:22.5px;color:var(--text)}
.who-btn{position:absolute;left:685px;top:2473px;height:46px;padding:0 26px;font-size:15px}

/* testimonials */
.testimonials{position:absolute;top:2606px;left:0;width:1200px;height:650px;background:var(--light)}
.tcard{position:absolute;top:128px;width:340px;height:298px;border-radius:4px;overflow:hidden}
.tcard .play{left:156px;top:135px;width:34px;height:34px}
.tname{position:absolute;top:440px;font-family:var(--body);font-weight:bold;font-size:16px}
.trole{position:absolute;top:464px;font-size:10px;color:#555}
.pager{position:absolute;top:527px;left:573px;display:flex;gap:14px}
.pager i{width:9px;height:9px;border-radius:50%;border:1px solid #999}
.pager i.on{background:var(--coral);border-color:var(--coral)}

/* footer */
.site-footer{position:absolute;top:3150px;left:0;width:1200px;height:552px;background:var(--black);color:#c9c9cc}
.foot-curve{position:absolute;top:-2px;left:0}
.foot-arrow{position:absolute;left:599px;top:68px;width:2px;height:120px;background:var(--coral)}
.foot-arrow::before{content:"";position:absolute;left:-6px;top:0;width:10px;height:10px;border-left:2px solid var(--coral);border-top:2px solid var(--coral);transform:rotate(45deg)}
.foot-brand{position:absolute;left:0;width:1200px;top:210px;display:flex;justify-content:center;align-items:center;gap:8px;font-size:28px;letter-spacing:1px;color:#cfcfd3}
.foot-brand .mark{width:12px;height:12px;border-radius:50%;background:var(--coral)}
.foot-col h4{font-family:var(--display);font-weight:400;font-size:14px;color:#d6d6d8;margin-bottom:14px}
.foot-col p{font-size:11px;line-height:26px;color:#a4a4a8}
.foot-divider{position:absolute;top:320px;width:2px;height:36px;background:var(--coral)}
.subscribe{margin-top:14px;width:301px;height:46px;border:1px solid #2c2c2e;display:flex;align-items:center;justify-content:space-between;padding:0 18px;font-size:11px;color:#555}
.subscribe .chev{color:var(--coral)}
.contact-row{display:flex;align-items:center;gap:18px;font-size:11px;color:#a4a4a8;margin-bottom:14px}
.contact-row i{width:12px;height:10px;background:#8a8a8e;border-radius:2px}
.copyright{position:absolute;left:176px;top:515px;font-size:11px;color:#4b4b4e}
.foot-social{position:absolute;left:884px;top:510px;display:flex;align-items:center;gap:10px;font-size:11px;color:#4b4b4e}
.foot-social i{width:18px;height:18px;border-radius:50%;background:#6d6d71}
</style>
</head>
<body>

<header class="site-header">
  <div class="brand"><span>BRIGHTPATH STUDIO</span><span class="mark"></span></div>
  <nav class="main-nav">
    <span class="active">Home</span><span>About us</span><span>Our Programs</span><span>Our Team</span><span>Contact Us</span>
  </nav>
  <div class="header-cta"><span class="bubble"></span>Make An Appointment</div>
</header>

<section class="hero" role="img" aria-label="Coach in conversation with a young couple in a bright office with a whiteboard"></section>
<div class="hero-copy">
  <div class="hero-kicker">watch a first coaching session &nbsp;›</div>
  <h1 class="hero-title">Only Brightpath Studio offers both life and career coaching programs</h1>
  <div class="btn hero-btn">Explore Our Programs <span class="chev"></span></div>
</div>
<div class="follow">Follow Us</div>
<div class="follow-line"></div>
<div class="follow-icons"><span></span><span></span><span></span></div>
<div class="play-video"></div>
<div class="play-label">Play Video</div>
<div class="play-arrow"></div>
<svg class="hero-curve" width="1200" height="120" viewBox="0 0 1200 120">
  <polygon points="0,120 0,112 600,8 1200,98 1200,120" fill="#ef6461"/>
  <polygon points="0,120 0,118 600,60 1200,118 1200,120" fill="#fff"/>
  <line x1="600" y1="4" x2="600" y2="64" stroke="#ef6461" stroke-width="2"/>
  <polyline points="594,56 600,64 606,56" fill="none" stroke="#ef6461" stroke-width="2"/>
</svg>

<h2 class="section-title" style="top:800px">Our Programs</h2>
<div class="program" style="left:173px;top:868px;background:linear-gradient(135deg,#c9c3b8,#8e7b63)" role="img" aria-label="Smiling coach at a desk holding a life balance sketch">
  <div class="shade"></div><div class="play play-lg"></div><span class="label">Life Coaching</span>
</div>
<div class="notch"></div><div class="notch-btn"></div>
<div class="program" style="left:611px;top:868px;background:linear-gradient(135deg,#7d7466,#3e3a35)" role="img" aria-label="Two professionals discussing career plans at a laptop">
  <div class="shade"></div><div class="play"></div><span class="label">Career Coaching</span>
</div>
<div class="program" style="left:173px;top:1215px;background:linear-gradient(135deg,#d4d2ce,#9d958b)" role="img" aria-label="Group coaching circle with a facilitator standing">
  <div class="shade"></div><div class="play"></div><span class="label">Group Coaching</span>
</div>
<div class="program" style="left:611px;top:1215px;background:linear-gradient(135deg,#6f6a62,#2f2b27)" role="img" aria-label="Couple shaking hands with a counsellor in a living room">
  <div class="shade"></div><div class="play"></div><span class="label">Relationship Coaching</span>
</div>

<section class="how">
  <h2 class="section-title">How it Works</h2>
  <svg class="abs" style="left:0;top:0" width="1200" height="423">
    <path d="M270 171 H928 H950 a93 93 0 0 1 0 186 H720" fill="none" stroke="rgba(255,255,255,.55)" stroke-width="1.2"/>
    <line x1="480" y1="352" x2="380" y2="352" stroke="rgba(255,255,255,.55)" stroke-width="1.2"/>
  </svg>
  <div class="step" style="left:170px">
    <div class="icon"><span class="num">01</span>
      <svg class="abs" style="left:17px;top:17px" width="34" height="34"><rect x="2" y="2" width="13" height="13" rx="4" fill="#ef6461"/><rect x="19" y="2" width="13" height="13" rx="4" fill="#ef6461"/><rect x="2" y="19" width="13" height="13" rx="4" fill="#ef6461"/><rect x="19" y="19" width="13" height="13" rx="4" fill="#ef6461"/></svg>
    </div>
    <h3>Choose a service</h3><p>Lorem ipsum dolor sit amet,<br>consectetur adipiscing elit tt.</p>
  </div>
  <div class="step" style="left:395px">
    <div class="icon"><span class="num">02</span>
      <svg class="abs" style="left:19px;top:16px" width="30" height="36"><circle cx="15" cy="10" r="7" fill="#ef6461"/><path d="M3 34 q0-14 12-14 q12 0 12 14z" fill="#ef6461"/></svg>
    </div>
    <h3>Book a career coach</h3><p>Lorem ipsum dolor sit amet,<br>consectetur adipiscing elit tt.</p>
  </div>
  <div class="step" style="left:603px">
    <div class="icon"><span class="num">03</span>
      <svg class="abs" style="left:18px;top:18px" width="34" height="32"><rect x="2" y="5" width="24" height="22" rx="3" fill="none" stroke="#ef6461" stroke-width="2.5"/><line x1="2" y1="12" x2="26" y2="12" stroke="#ef6461" stroke-width="2.5"/><circle cx="25" cy="23" r="7" fill="#fff" stroke="#ef6461" stroke-width="2.5"/></svg>
    </div>
    <h3>Decide on a time</h3><p>Lorem ipsum dolor sit amet,<br>consectetur adipiscing elit tt.</p>
  </div>
  <div class="step" style="left:828px">
    <div class="icon"><span class="num">04</span>
      <svg class="abs" style="left:20px;top:18px" width="30" height="32"><path d="M24 3 C14 5 9 13 8 19 l5 5 C19 22 26 17 27 6z" fill="#ef6461"/><path d="M8 21 l-5 8 l8-5z" fill="#ef6461"/></svg>
    </div>
    <h3>Get started!</h3><p>Lorem ipsum dolor sit amet,<br>consectetur adipiscing elit tt.</p>
  </div>
  <div class="btn how-btn">Make An Appointment <span class="chev"></span></div>
</section>

<div class="dots" style="left:484px;top:2196px;grid-template-columns:repeat(3,4px)"><i></i><i></i><i></i><i></i><i></i><i></i></div>
<div class="dots" style="left:260px;top:2416px;grid-template-columns:repeat(4,4px);gap:20px 26px"><i></i><i></i><i></i><i></i><i></i><i></i><i></i><i></i><i></i><i></i><i></i><i></i></div>
<div class="abs" style="left:364px;top:2232px;width:271px;height:288px;background:linear-gradient(160deg,#c9b8a3,#7a6a5a 60%,#3e3934)" role="img" aria-label="Two hikers helping each other up a rocky ridge at sunset"></div>
<div class="abs" style="left:172px;top:2117px;width:294px;height:287px;background:linear-gradient(135deg,#e6e3dd,#b8b2a6 55%,#6b5f8a)" role="img" aria-label="Client and coach in a conversation on a sofa"></div>
<h2 class="who-title">Who We Are</h2>
<p class="who-text" style="top:2156px">Lorem ipsum dolor sit amet, consectetur adipiscing elit, sed do eiusmod tempor incididunt ut labore et dolore magna aliqua. Ut enim ad minim veniam, quis nostrud exercitation ullamco laboris nisi ut aliquip ex ea commodo consequat. Duis aute irure dolor in reprehenderit in voluptate velit esse cillum dolore eu fugiat nulla pariatur. Excepteur sint occaecat cupidatat non proident, sunt in culpa qui officia deserunt mollit anim id est laborum.</p>
<p class="who-text" style="top:2352px">Lorem ipsum dolor sit amet, consectetur adipiscing elit, sed do eiusmod tempor incididunt ut labore et dolore magna aliqua. Ut enim ad minim veniam, quis nostrud exercitation ullamco laboris nisi ut aliquip.</p>
<div class="btn who-btn">Make An Appointment <span class="chev"></span></div>

<section class="testimonials">
  <h2 class="section-title" style="top:60px">Client Testimonials</h2>
  <div class="tcard" style="left:68px;background:linear-gradient(160deg,#6f8a5e,#c9c2b6 60%,#d14a40)" role="img" aria-label="Portrait of a smiling businesswoman outdoors"><div class="play"></div></div>
  <div class="tcard" style="left:430px;background:linear-gradient(160deg,#c7c7c5,#7b97bd 60%,#3e5f8d)" role="img" aria-label="Portrait of a man in a denim shirt in a kitchen"><div class="play"></div></div>
  <div class="tcard" style="left:791px;background:linear-gradient(160deg,#b96d7a,#8a7a66 55%,#a9b8cf)" role="img" aria-label="Portrait of a young woman among blossoms"><div class="play"></div></div>
  <div class="tname" style="left:70px">Dana Keller</div><div class="trole" style="left:70px">Managing Director</div>
  <div class="tname" style="left:431px">Tomas Verhoef</div><div class="trole" style="left:431px">Financial Advisor</div>
  <div class="tname" style="left:791px">Lena Ortiz</div><div class="trole" style="left:791px">CEO Co-Founder</div>
  <div class="pager"><i></i><i class="on"></i><i></i></div>
</section>

<footer class="site-footer">
  <svg class="foot-curve" width="1200" height="110" viewBox="0 0 1200 110">
    <polygon points="0,0 1200,0 1200,8 600,104 0,10" fill="#ef6461"/>
    <polygon points="0,0 1200,0 1200,0 600,80 0,0" fill="#f5f5f6"/>
  </svg>
  <div class="foot-arrow"></div>
  <div class="foot-brand"><span>BRIGHTPATH STUDIO</span><span class="mark"></span></div>

  <div class="foot-col abs" style="left:174px;top:318px">
    <h4>Office</h4>
    <p>Germany —<br>212 Harlow Lane, Suite 19<br>Lindenau, De 40210</p>
  </div>
  <div class="foot-divider" style="left:392px"></div>
  <div class="foot-col abs" style="left:447px;top:318px">
    <h4>Connect</h4>
    <p>Receive updates from Elin straight to your inbox.</p>
    <div class="subscribe"><span>Email Address</span><span class="chev"></span></div>
  </div>
  <div class="foot-divider" style="left:787px"></div>
  <div class="foot-col abs" style="left:852px;top:318px">
    <h4>Phone &amp; Email address</h4>
    <div class="contact-row"><i></i>hello@brightpath.example</div>
    <div class="contact-row"><i style="border-radius:50%"></i>+1 555 017 42 88</div>
  </div>

  <div class="copyright">© 2024 Brightpath Studio. All Rights Reserved.</div>
  <div class="foot-social">Follow Us : <i></i><i></i><i></i></div>
</footer>

</body>
</html>
```